Tervolan Pty Ltd professional business card

A professional business card template using the colours from the supplied logo.
Clean crisp lines while, Modern while not being over the top.

Target Market(s)

Construction, commerical and industrial

Industry/Entity Type

Communications

Contact Information for Business Card

For a Communications, IT, Optical fibre installation company

Colors
37b8a4

```html
<!DOCTYPE html>
<html lang="en">
<head>
<meta charset="utf-8">
<title>Tervolan Pty Ltd – Business Card</title>
<link rel="stylesheet" href="https://fonts.googleapis.com/css2?family=Montserrat:wght@500;600&family=Roboto+Condensed:wght@400&family=Open+Sans:wght@400&display=swap">
<style>
  :root {
    --backdrop: #ececea;
    --card-light: #ffffff;
    --card-mid: #ececed;
    --card-shade: #dedee0;
    --teal: #37b8a4;
    --teal-deep: #2a9c8a;
    --ink: #6d6e71;
    --ink-soft: #8a8b8e;
    --rule: #9a9a9c;
  }
  * { margin: 0; padding: 0; box-sizing: border-box; }
  html, body {
    width: 1200px; height: 1200px; overflow: hidden;
    background: var(--backdrop);
  }
  .canvas { position: relative; width: 1200px; height: 1200px; }

  .card {
    position: absolute;
    left: 300px; width: 600px; height: 341px;
    overflow: hidden;
    background: var(--card-light);
    box-shadow: 0 3px 10px rgba(0,0,0,0.18);
  }
  .card-front { top: 192px; }
  .card-back { top: 588px; }

  .card-surface {
    position: absolute; inset: 0;
    background: linear-gradient(135deg, var(--card-light) 0%, var(--card-mid) 60%, var(--card-shade) 100%);
  }
  .card-back .card-surface {
    background: linear-gradient(160deg, var(--card-light) 0%, var(--card-light) 50%, var(--card-mid) 100%);
  }
  .card-footer-band {
    position: absolute; left: 0; right: 0; bottom: 0; height: 70px;
    background: linear-gradient(90deg, var(--teal-deep) 0%, var(--teal) 45%, var(--teal) 100%);
  }

  .brand {
    position: absolute;
    display: flex; align-items: center;
    font-family: "Montserrat", sans-serif;
    font-weight: 600;
    color: var(--ink);
    letter-spacing: 0.5px;
    line-height: 1;
  }
  .brand-dot { border-radius: 50%; background: var(--teal); flex: none; }
  .card-front .brand { left: 0; right: 0; top: 138px; justify-content: center; font-size: 62px; gap: 16px; }
  .card-front .brand-dot { width: 30px; height: 30px; }
  .card-back .brand { left: 50px; top: 108px; font-size: 36px; gap: 10px; }
  .card-back .brand-dot { width: 18px; height: 18px; }

  .divider { position: absolute; left: 317px; top: 84px; width: 1.5px; height: 160px; background: var(--rule); }

  .person { position: absolute; left: 350px; top: 86px; }
  .person-name { font-family: "Montserrat", sans-serif; font-weight: 500; font-size: 29px; color: var(--ink); letter-spacing: 1px; line-height: 1; }
  .person-role { font-family: "Roboto Condensed", sans-serif; font-size: 15px; color: var(--teal); letter-spacing: 1.5px; margin-top: 6px; text-transform: uppercase; }

  .contacts { position: absolute; left: 350px; top: 160px; list-style: none; }
  .contact { display: flex; align-items: center; gap: 14px; height: 28px; font-family: "Open Sans", sans-serif; font-size: 10px; color: var(--ink-soft); }
  .contact svg { width: 12px; height: 12px; fill: var(--teal); flex: none; }
</style>
</head>
<body>
<main class="canvas">

  <section class="card card-front" aria-label="Card front">
    <div class="card-surface" role="img" aria-label="Soft grey layered background artwork"></div>
    <div class="brand"><span class="brand-dot"></span>Tervolan</div>
  </section>

  <section class="card card-back" aria-label="Card back">
    <div class="card-surface" role="img" aria-label="Soft light grey background artwork"></div>
    <div class="card-footer-band" role="img" aria-label="Teal and grey decorative footer band"></div>

    <div class="brand"><span class="brand-dot"></span>Tervolan</div>
    <div class="divider"></div>

    <div class="person">
      <div class="person-name">NAME</div>
      <div class="person-role">Account Manager</div>
    </div>

    <ul class="contacts">
      <li class="contact">
        <svg viewBox="0 0 24 24" aria-hidden="true"><path d="M6.6 10.8a15.5 15.5 0 0 0 6.6 6.6l2.2-2.2c.3-.3.7-.4 1-.2 1.1.4 2.3.6 3.6.6.6 0 1 .4 1 1V20c0 .6-.4 1-1 1C10.6 21 3 13.4 3 4c0-.6.4-1 1-1h3.5c.6 0 1 .4 1 1 0 1.3.2 2.5.6 3.6.1.3 0 .7-.2 1z"/></svg>
        <span>+00 000 000 000</span>
      </li>
      <li class="contact">
        <svg viewBox="0 0 24 24" aria-hidden="true"><path d="M2 5h20v14H2z"/></svg>
        <span>name@tervolan.com.au</span>
      </li>
      <li class="contact">
        <svg viewBox="0 0 24 24" aria-hidden="true"><path d="M12 2a7 7 0 0 0-7 7c0 5.2 7 13 7 13s7-7.8 7-13a7 7 0 0 0-7-7zm0 9.5A2.5 2.5 0 1 1 12 6.5a2.5 2.5 0 0 1 0 5z"/></svg>
        <span>123 street, Australia</span>
      </li>
    </ul>
  </section>

</main>
</body>
</html>
```